Looking for a clean, modern, and professional business card design that reflects Valtrin Systems

The design should include the company logo, contact details, and align with our brand identity. Please use a sophisticated and minimalist style, incorporating [specific colors, if applicable]. Creativity is welcome, but the card must maintain a polished and professional appearance.

Details to Include:

Name: Lou Marchetti
Title: VP Sales / Operations
Company: Valtrin Systems
Phone: 304.617.2285
Email: lou@valtrinsystems.example
Website: www.valtrinsystems.example

```html
<!DOCTYPE html>
<html lang="en">
<head>
<meta charset="utf-8">
<title>Valtrin Systems – Business Card</title>
<link rel="stylesheet" href="https://fonts.googleapis.com/css2?family=Poppins:wght@400;500;600&display=swap">
<style>
  :root {
    --stage: #bdbec0;
    --paper: #ffffff;
    --ink: #050709;
    --brand-blue: #3273b8;
    --white: #ffffff;
  }
  * { margin: 0; padding: 0; box-sizing: border-box; }
  html, body {
    width: 1200px; height: 900px; overflow: hidden;
    background: var(--stage);
    font-family: "Poppins", sans-serif;
  }
  .card {
    position: absolute;
    top: 322px;
    width: 473px; height: 271px;
    overflow: hidden;
  }
  .card--front { left: 132px; background: var(--paper); }
  .card--back  { left: 624px; background: var(--ink); }

  .wordmark {
    position: absolute;
    font-weight: 600;
    white-space: nowrap;
    letter-spacing: 0.01em;
    line-height: 1;
  }
  .card--front .wordmark { left: 16px; top: 44px; font-size: 20px; color: var(--ink); }
  .card--back .wordmark  { left: 248px; top: 130px; font-size: 23px; color: var(--white); }

  .person-name {
    position: absolute; left: 16px; top: 140px;
    font-size: 23px; font-weight: 500; color: var(--brand-blue);
    line-height: 1;
  }
  .name-rule {
    position: absolute; left: 0; top: 164px;
    width: 375px; height: 1px; background: var(--brand-blue);
  }
  .person-title {
    position: absolute; left: 17px; top: 166px;
    font-size: 12px; color: var(--ink);
  }
  .contact-list { list-style: none; position: absolute; left: 17px; top: 200px; }
  .contact-list li {
    display: flex; align-items: center; gap: 12px;
    height: 18px; font-size: 11.5px; color: var(--brand-blue);
  }
  .contact-list li + li { margin-top: 0.5px; }
  .contact-icon { width: 12px; height: 12px; flex: none; }

  .bar { position: absolute; height: 15px; }
  .card--front .bar { right: 0; background: var(--brand-blue); }
  .card--back .bar  { left: 0; background: var(--white); }
</style>
</head>
<body>
  <section class="card card--front" aria-label="Business card front">
    <div class="wordmark">Valtrin Systems</div>

    <div class="bar" style="top:44px;width:49px"></div>
    <div class="bar" style="top:71px;width:73px"></div>
    <div class="bar" style="top:100px;width:92px"></div>

    <h1 class="person-name">Lou Marchetti</h1>
    <div class="name-rule"></div>
    <p class="person-title">VP Sales / Operations</p>

    <ul class="contact-list">
      <li>
        <svg class="contact-icon" viewBox="0 0 12 12" aria-hidden="true">
          <circle cx="6" cy="6" r="6" fill="var(--ink)"/>
          <path d="M4 3.2c.3-.2.6-.1.8.2l.5.8c.1.3 0 .5-.2.7l-.3.2c.3.7.8 1.2 1.5 1.5l.2-.3c.2-.2.4-.3.7-.2l.8.5c.3.2.4.5.2.8-.4.6-1 .8-1.6.5C5.4 7.4 4.6 6.6 4 5.4c-.3-.7-.3-1.6 0-2.2z" fill="var(--white)"/>
        </svg>
        304.617.2285
      </li>
      <li>
        <svg class="contact-icon" viewBox="0 0 12 12" aria-hidden="true">
          <circle cx="6" cy="6" r="6" fill="var(--ink)"/>
          <rect x="3" y="4" width="6" height="4.2" fill="none" stroke="var(--white)" stroke-width=".8"/>
          <path d="M3 4l3 2.3L9 4" fill="none" stroke="var(--white)" stroke-width=".8"/>
        </svg>
        lou@valtrinsystems.example
      </li>
      <li>
        <svg class="contact-icon" viewBox="0 0 12 12" aria-hidden="true">
          <circle cx="6" cy="6" r="6" fill="var(--ink)"/>
          <g fill="none" stroke="var(--white)" stroke-width=".6">
            <circle cx="6" cy="6" r="3"/>
            <ellipse cx="6" cy="6" rx="1.3" ry="3"/>
            <path d="M3 6h6"/>
          </g>
        </svg>
        www.valtrinsystems.example
      </li>
    </ul>
  </section>

  <section class="card card--back" aria-label="Business card back">
    <div class="bar" style="top:150px;width:91px"></div>
    <div class="bar" style="top:180px;width:72px"></div>
    <div class="bar" style="top:207px;width:48px"></div>
    <div class="wordmark">Valtrin Systems</div>
  </section>
</body>
</html>
```